Motivational Poster Design Project

I would like to create a poster with some of my favorite quotes to hang in my office. I did a similar project in 2012 and I've uploaded the top 2 designs so you can get a better idea of what I'm looking for. I will provide feedback on your design within 24 hours of receiving it.

The poster must contain the following quotes:

"You’re only given a little spark of madness. You mustn’t lose it.”
- Dorian Falkes

“The most contrarian thing of all is not to oppose the crowd but to think for yourself.”
- Miles Crand

"I constantly see people rise in life who are not the smartest, sometimes not even the most diligent, but they are learning machines. They go to bed every night a little wiser than they were when they got up and boy does that help, particularly when you have a long run ahead of you."
- Harvey Belcott

“In theory, there’s no difference between theory and practice. But, in practice, there is.”
- Kees R. T. Ter Hoogwater

"At the end of the day, a reactionary life is a normal life. One thing is consistent in every remarkable person: they decide to do something remarkable. Don’t let the world choose who you become."
- Darvesh Kulani

“It usually takes 3-4 months to try enough that you can do a proper 80/20 analysis, then two months to design systems to scale what *is* working.”
-Ned Gowlan

“Authority is 20 percent given, 80 percent taken.”
- Harold Finchamp

“Your actions are consistent with the way the world occurs to you.”
- Gustav Lemmke
Updates

Project Deadline Extended
Reason: I am going to be travelling with no access to internet until January 5th, 2015. I am extending the project deadline until 12/31/14 and I'll make a final decision during the 1st week of January.

Target Market(s)

Personal Project

Industry/Entity Type

Learning

Requirements
Must have
• The poster will be 24" high x 36" long and printed on canvas, so the image you create needs to have a resolution of at least 2700 x 3900.
Nice to have
• I don't have an exact vision for how the poster should look, so I am totally open to you using your creativity to develop, arrange and present the content as you'd like.
• That said, I would like an image (photo or posterized image) of the person being quoted along with each quote. I do not have specific images that I would like you to use, so you will need to find the images on your own. The images don't need to be perfect... I am more interested in the poster relating the essence of the quotes and the people being quoted than I am in perfect photographic images of the people being quoted.

```html
<!DOCTYPE html>
<html lang="en">
<head>
<meta charset="utf-8">
<title>Favourite Quotes Poster</title>
<link rel="stylesheet" href="https://fonts.googleapis.com/css2?family=Open+Sans:wght@300;400;700;800&family=Roboto:wght@400;500;700&display=swap">
<style>
  :root {
    --paper: #ffffff;
    --ink-grey: #8a8a8a;
    --ink-dark: #333333;
    --quote-red: #ef5a5a;
    --violet: #5a5fa6;
    --sky: #3d87c7;
    --lilac: #a86bb8;
    --purple: #8b4a9c;
    --lime: #8dc63f;
    --green: #2f9a4a;
    --teal: #2bb0a0;
    --tan: #c4a173;
    --brown: #8a6846;
    --blue: #2f7fc1;
    --red: #e2312b;
    --crimson: #b5222d;
    --navy: #1f5fa8;
    --orange: #e8741e;
    --tri-violet: #b9a8d6;
    --tri-sky: #a9cbe8;
    --tri-green: #7cc39b;
    --tri-brown: #a8907a;
    --tri-blue: #6ea6d8;
    --tri-salmon: #f39a80;
    --tri-amber: #f0bd78;
  }
  html, body {
    margin: 0; padding: 0;
    width: 872px; height: 1200px; overflow: hidden;
  }
  body {
    background: var(--paper);
    font-family: "Roboto", Arial, sans-serif;
  }
  .poster { position: relative; width: 872px; height: 1200px; overflow: hidden; }
  .decor { position: absolute; left: 0; top: 0; width: 872px; height: 1200px; }
  .ln {
    position: absolute; margin: 0; white-space: nowrap;
    line-height: 1; font-weight: 700; color: var(--ink-grey); font-size: 16px;
    transform: translate(-50%, -50%);
  }
  .ln.right { transform: translate(-100%, -50%); }
  .big { font-family: "Open Sans", Arial, sans-serif; font-weight: 800; }
  .light { font-family: "Open Sans", Arial, sans-serif; font-weight: 300; }
  .regular { font-weight: 400; }
  .mark { color: var(--quote-red); font-family: "Open Sans", Arial, sans-serif; font-weight: 800; }
  .author { font-weight: 400; font-size: 10px; color: var(--ink-dark); }
</style>
</head>
<body>
<main class="poster">
  <svg class="decor" viewBox="0 0 872 1200" aria-hidden="true">
    <g opacity=".6">
      <polygon points="52,0 150,0 98,74" fill="var(--tri-violet)"/>
      <polygon points="100,0 150,0 128,40" fill="var(--tri-violet)"/>
      <polygon points="0,141 124,228 0,308" fill="var(--tri-violet)"/>
      <polygon points="10,170 70,215 10,250" fill="var(--tri-violet)"/>
      <polygon points="20,282 65,288 20,304" fill="var(--tri-violet)"/>
      <polygon points="143,355 182,315 215,382" fill="var(--tri-green)"/>
      <polygon points="160,360 185,335 205,372" fill="var(--tri-green)"/>
      <polygon points="656,27 806,7 735,134" fill="var(--tri-sky)"/>
      <polygon points="700,30 780,20 745,90" fill="var(--tri-sky)"/>
      <polygon points="872,194 728,261 872,342" fill="var(--tri-sky)"/>
      <polygon points="820,240 760,300 840,330" fill="var(--tri-sky)"/>
      <polygon points="657,563 735,536 722,610" fill="var(--tri-green)"/>
      <polygon points="680,565 730,550 720,595" fill="var(--tri-green)"/>
      <polygon points="0,556 137,623 0,690" fill="var(--tri-brown)"/>
      <polygon points="30,570 80,590 35,620" fill="var(--tri-brown)"/>
      <polygon points="20,640 90,655 30,685" fill="var(--tri-brown)"/>
      <polygon points="660,804 708,804 682,865" fill="var(--tri-blue)"/>
      <polygon points="472,885 533,891 507,931" fill="var(--tri-blue)"/>
      <polygon points="0,1025 111,1079 13,1146" fill="var(--tri-salmon)"/>
      <polygon points="10,1050 70,1075 20,1110" fill="var(--tri-salmon)"/>
      <polygon points="319,1126 267,1200 371,1200" fill="var(--tri-amber)"/>
      <polygon points="330,1150 300,1200 360,1200" fill="var(--tri-amber)"/>
      <polygon points="872,1025 728,1106 872,1186" fill="var(--tri-green)"/>
      <polygon points="850,1070 770,1110 850,1150" fill="var(--tri-green)"/>
    </g>
  </svg>

  <section class="quote quote-spark">
    <p class="ln light" style="left:312px;top:70px;font-size:22px;font-weight:400"><span class="mark">“</span>You're only given a</p>
    <p class="ln big" style="left:390px;top:97px;font-size:30px;color:var(--violet)">little spark</p>
    <p class="ln" style="left:390px;top:121px;font-size:15px;color:var(--violet)">of</p>
    <p class="ln big" style="left:390px;top:143px;font-size:31px;color:var(--violet)">madness.</p>
    <p class="ln big" style="left:489px;top:176px;font-size:37px;font-weight:700;color:var(--sky)">You mustn't lose it.<span class="mark">”</span></p>
    <p class="ln author right" style="left:680px;top:206px">- Dorian Falkes</p>
  </section>

  <section class="quote quote-contrarian">
    <p class="ln" style="left:332px;top:254px;font-size:17px"><span class="mark">“</span>The most contrarian thing</p>
    <p class="ln" style="left:287px;top:275px;font-size:17px">of all is not to</p>
    <p class="ln light" style="left:338px;top:294px;font-size:26px;color:var(--lilac)">oppose the</p>
    <p class="ln big" style="left:365px;top:318px;font-size:34px;color:var(--purple)">crowd</p>
    <p class="ln" style="left:468px;top:322px;font-size:15px">but to</p>
    <p class="ln big" style="left:567px;top:324px;font-size:26px;color:var(--purple)">think for</p>
    <p class="ln big" style="left:643px;top:348px;font-size:26px;color:var(--purple)">yourself.<span class="mark">”</span></p>
    <p class="ln author right" style="left:767px;top:372px">- Miles Crand</p>
  </section>

  <section class="quote quote-learning">
    <p class="ln" style="left:424px;top:414px">"I constantly see <span class="big" style="font-size:30px;color:var(--lime)">people rise in life</span> who are not the</p>
    <p class="ln" style="left:422px;top:443px"><span class="big" style="font-size:24px;color:var(--green)">smartest</span>, sometimes not even the <span class="big" style="font-size:24px;color:var(--green)">most diligent</span>, but</p>
    <p class="ln" style="left:412px;top:467px">they are <span class="regular" style="color:var(--teal)">learning machines</span>. They go to bed every night a</p>
    <p class="ln big" style="left:524px;top:492px;font-size:32px;color:var(--lime)">little wiser</p>
    <p class="ln" style="left:421px;top:518px">than they were when they got up and boy does that help, particularly</p>
    <p class="ln" style="left:322px;top:538px">when you have a long run ahead of you."</p>
    <p class="ln author" style="left:526px;top:555px">- Harvey Belcott</p>
  </section>

  <section class="quote quote-theory">
    <p class="ln" style="left:408px;top:620px;font-size:17px;color:var(--tan)"><span class="mark">“</span>In theory, there's <span class="big" style="font-size:28px">no difference</span> between</p>
    <p class="ln big" style="left:415px;top:652px;font-size:39px;color:var(--brown)">theory <span class="light" style="font-size:27px;font-weight:400">and</span> practice.</p>
    <p class="ln" style="left:446px;top:683px;font-size:14px;color:var(--tan)">But,</p>
    <p class="ln big" style="left:596px;top:696px;font-size:30px;color:var(--tan)">in practice,</p>
    <p class="ln big" style="left:637px;top:728px;font-size:39px;color:var(--brown)">there is.<span class="mark" style="font-size:22px">”</span></p>
    <p class="ln author" style="left:692px;top:756px">- Kees R. T. Ter Hoogwater</p>
  </section>

  <section class="quote quote-remarkable">
    <p class="ln" style="left:152px;top:734px;font-size:15px">"At the end of the day, a</p>
    <p class="ln" style="left:213px;top:755px;font-size:15px"><span class="big" style="font-size:23px;color:var(--blue)">reactionary life</span> is a</p>
    <p class="ln big" style="left:315px;top:780px;font-size:34px;color:var(--red)">normal life.</p>
    <p class="ln" style="left:263px;top:806px;font-size:15px">One thing is consistent in every <span class="big" style="font-size:21px;color:var(--blue)">remarkable person:</span></p>
    <p class="ln" style="left:326px;top:828px;font-size:15px">they decide to do something <span class="big" style="font-size:21px;color:var(--red)">remarkable</span>.</p>
    <p class="ln" style="left:261px;top:848px;font-size:15px">Don't let the world choose who you become."</p>
    <p class="ln author" style="left:490px;top:864px">- Darvesh Kulani</p>
  </section>

  <section class="quote quote-analysis">
    <p class="ln" style="left:238px;top:946px;font-size:16px">"It usually takes <span class="big" style="font-size:28px;color:var(--crimson)">3-4</span> months to try enough</p>
    <p class="ln" style="left:282px;top:969px;font-size:16px">that you can do a proper <span class="big" style="font-size:23px;color:var(--crimson)">80/20</span> analysis,</p>
    <p class="ln" style="left:290px;top:987px;font-size:16px">then two months to design systems to scale</p>
    <p class="ln big" style="left:324px;top:1014px;font-size:32px;color:var(--crimson)">what *is* working.”</p>
    <p class="ln author" style="left:546px;top:1038px">-Ned Gowlan</p>
  </section>

  <section class="quote quote-authority">
    <p class="ln regular" style="left:673px;top:902px;font-size:19px;color:var(--ink-dark)">“Authority is</p>
    <p class="ln big" style="left:673px;top:937px;font-size:35px;color:var(--navy)">20</p>
    <p class="ln regular" style="left:673px;top:969px;font-size:18px;color:var(--navy)">percent given,</p>
    <p class="ln big" style="left:673px;top:1004px;font-size:35px;color:var(--navy)">80</p>
    <p class="ln regular" style="left:673px;top:1034px;font-size:18px;color:var(--navy)">percent taken.”</p>
    <p class="ln author" style="left:746px;top:1054px">- Harold Finchamp</p>
  </section>

  <section class="quote quote-actions">
    <p class="ln big" style="left:361px;top:1083px;font-size:26px;color:var(--orange)">“Your actions</p>
    <p class="ln regular" style="left:392px;top:1100px;font-size:13px;color:var(--orange)">are consistent with the way the</p>
    <p class="ln big" style="left:540px;top:1118px;font-size:26px;color:var(--orange)">world occurs <span class="regular" style="font-family:Roboto, Arial, sans-serif;font-size:13px;vertical-align:8px">to</span></p>
    <p class="ln big" style="left:585px;top:1142px;font-size:26px;color:var(--orange)">you.”</p>
    <p class="ln author" style="left:673px;top:1146px">-Gustav Lemmke</p>
  </section>
</main>
</body>
</html>
```